Business Card Velostra - Accounting firm

Hi my friend.
I'm coming back to you to see if it would be possible for you to make a modern and minimalist business card design.
In shades of blue like the great logo you offered me.
The ideal is a modern and aesthetic business card.
The goal is to give a professional effect to the first exchanges.
Renewal and innovation in the accounting world !!
I thank you !!
Good evening to you

Target Market(s)

Young, dynamic and sensitive to marketing

Industry/Entity Type

Finance And Accounting

Contact Information for Business Card

Company logo and name. Last name, First name, Phone number, email address, company address, website.

Font styles to use
Sans Serif

Requirements
Must have
• The ideal is a modern and aesthetic business card.

Mentions to include: Company logo and name. Last name, First name, Phone number, email address, company address, website.
Nice to have
• The goal is to give a professional effect to the first exchanges.
Should not have
• Simplistic or childish design

```html
<!DOCTYPE html>
<html lang="en">
<head>
<meta charset="utf-8">
<title>Velostra – Business Card</title>
<link rel="stylesheet" href="https://fonts.googleapis.com/css2?family=Montserrat:wght@600&family=Source+Sans+3:wght@400;600;700&display=swap">
<style>
  :root {
    --page-bg: #e4e4e4;
    --navy: #1f2b5e;
    --navy-deep: #0b1640;
    --teal: #5bbcae;
    --blue: #1171bd;
    --mark: #3a9fb5;
    --card-light: #f4f4f4;
    --ink: #2a2a2a;
  }
  html, body {
    margin: 0;
    width: 1200px;
    height: 960px;
    overflow: hidden;
    background: var(--page-bg);
  }
  .canvas {
    position: relative;
    width: 1200px;
    height: 960px;
  }
  .card {
    position: absolute;
    left: 300px;
    width: 597px;
    height: 342px;
    overflow: hidden;
  }
  /* Front side */
  .card-front {
    top: 117px;
    background: var(--navy);
  }
  .front-pattern {
    position: absolute;
    inset: 0;
    background: linear-gradient(100deg, #6f93ab 0%, #3f5a86 30%, #22336a 60%, var(--navy-deep) 100%);
    opacity: 0.9;
  }
  .front-brand {
    position: absolute;
    left: 337px;
    top: 210px;
    display: flex;
    align-items: center;
    gap: 10px;
  }
  .brand-square {
    width: 55px;
    height: 54px;
    background: var(--mark);
    border-radius: 4px;
  }
  .front-brand .brand-name {
    font-family: "Montserrat", sans-serif;
    font-weight: 600;
    font-size: 42px;
    color: #ffffff;
    letter-spacing: -0.5px;
    line-height: 1;
  }
  /* Back side */
  .card-back {
    top: 510px;
    background: var(--card-light);
    font-family: "Source Sans 3", sans-serif;
    color: var(--ink);
  }
  .back-mark {
    position: absolute;
    left: 82px;
    top: 33px;
    width: 100px;
    height: 100px;
    background: var(--mark);
    border-radius: 6px;
  }
  .back-brand {
    position: absolute;
    left: 46px;
    top: 152px;
    font-family: "Montserrat", sans-serif;
    font-weight: 600;
    font-size: 38px;
    color: var(--navy);
    letter-spacing: -0.5px;
    line-height: 1;
  }
  .person {
    position: absolute;
    left: 47px;
    top: 248px;
  }
  .person-name {
    font-weight: 700;
    font-size: 20px;
    color: var(--navy);
    margin: 0;
    line-height: 1.2;
  }
  .person-title {
    font-size: 15px;
    margin: 2px 0 0;
  }
  .address {
    position: absolute;
    left: 340px;
    top: 167px;
    font-size: 15px;
    line-height: 20px;
    margin: 0;
    font-style: normal;
  }
  .contacts {
    position: absolute;
    left: 340px;
    top: 231px;
    list-style: none;
    margin: 0;
    padding: 0;
    font-size: 15px;
    line-height: 20px;
  }
  .contacts li {
    display: flex;
    align-items: center;
    gap: 7px;
  }
  .contacts svg {
    width: 13px;
    height: 13px;
    fill: var(--navy);
  }
  .band {
    position: absolute;
    left: 0;
    bottom: 0;
    width: 597px;
    height: 19px;
  }
</style>
</head>
<body>
<div class="canvas">

  <section class="card card-front" aria-label="Card front">
    <div class="front-pattern" role="img" aria-label="Decorative repeating pattern in blue tones, fading from light steel blue to deep navy"></div>
    <div class="front-brand">
      <span class="brand-square"></span>
      <span class="brand-name">velostra</span>
    </div>
  </section>

  <section class="card card-back" aria-label="Card back">
    <div class="back-mark"></div>
    <div class="back-brand">velostra</div>

    <div class="person">
      <p class="person-name">Daniel Moreau</p>
      <p class="person-title">President</p>
    </div>

    <address class="address">48 Harbor Crest Lane, Suite 310<br>Tampa, Florida, 33602</address>

    <ul class="contacts">
      <li>
        <svg viewBox="0 0 24 24" aria-hidden="true"><path d="M6.6 10.8a15.1 15.1 0 0 0 6.6 6.6l2.2-2.2c.3-.3.7-.4 1-.2 1.1.4 2.3.6 3.6.6.6 0 1 .4 1 1V20c0 .6-.4 1-1 1A17 17 0 0 1 3 4c0-.6.4-1 1-1h3.5c.6 0 1 .4 1 1 0 1.3.2 2.5.6 3.6.1.3 0 .7-.2 1z"/></svg>
        (555) 284-1937
      </li>
      <li>
        <svg viewBox="0 0 24 24" aria-hidden="true"><path d="M2 5h20v14H2zm2 2v.4l8 5.2 8-5.2V7zm0 2.8V17h16V9.8l-8 5.2z"/></svg>
        daniel@velostraweb.com
      </li>
      <li>
        <svg viewBox="0 0 24 24" aria-hidden="true"><path d="M12 2a10 10 0 1 0 0 20 10 10 0 0 0 0-20zm6.9 6h-3a15 15 0 0 0-1.3-3.9A8 8 0 0 1 18.9 8zM12 4c.8 1.1 1.5 2.5 1.9 4h-3.8c.4-1.5 1.1-2.9 1.9-4zM4.3 14a8 8 0 0 1 0-4h3.4a16 16 0 0 0 0 4zm.8 2h3a15 15 0 0 0 1.3 3.9A8 8 0 0 1 5.1 16zm3-8h-3a8 8 0 0 1 4.3-3.9C8.8 5.3 8.4 6.6 8.1 8zM12 20c-.8-1.1-1.5-2.5-1.9-4h3.8c-.4 1.5-1.1 2.9-1.9 4zm2.3-6H9.7a14 14 0 0 1 0-4h4.6a14 14 0 0 1 0 4zm.3 5.9c.6-1.2 1-2.5 1.3-3.9h3a8 8 0 0 1-4.3 3.9zm1.7-5.9a16 16 0 0 0 0-4h3.4a8 8 0 0 1 0 4z"/></svg>
        www.velostraweb.com
      </li>
    </ul>

    <svg class="band" viewBox="0 0 597 19" preserveAspectRatio="none" aria-hidden="true">
      <defs>
        <linearGradient id="bandGradient" x1="0" y1="0" x2="1" y2="0">
          <stop offset="0" stop-color="#4aaab4"/>
          <stop offset="1" stop-color="#1171bd"/>
        </linearGradient>
      </defs>
      <polygon points="0,0 334,0 316,19 0,19" fill="#1f2b5e"/>
      <polygon points="340,0 597,0 597,19 322,19" fill="url(#bandGradient)"/>
    </svg>
  </section>

</div>
</body>
</html>
```